New Website for Crime Scene Cleaner required

I need someone to create a complete new website and can set up SEO for me through the Website Designer or a third party for me. I have Logo that i will upload shortly once finalized for the website. I have domain names already but will need to be registered by the winner(i can supply the details I have received from NetHarbor). I am looking for a website that stands out but is simple and elegant, easy to navigate and use yet not boring. Using information provided by me for wording to create it as a stand out website. in total i am looking at 5-7 pages (About/Home, Fire & Smoke Restoration, Water Restoration/Mould Remediation, Crime Scene Cleaners, Methamphetamine Remediation/ Testing Services, Hoarding & Squalor Cleaning, Contact Us/Testimonials)This will be a start to finish project. I would like assistance to have it set up user friendly on mobile devices etc or refer a third party who can assist. Must be able to provide ongoing support when required by myself if the successful winner (i understand this will be an additional fee if required in the future).
You will also require to assist me with the email set up for the website so that it is fully functional or provide a third party who can.
To gain some information about the business you can visit my old website at www.pelgrosvandree.com.au and welcome to use some of the wording from there for your entry.
It's been 14yrs since i've had a website made from me so suggestions are welcome if not mentioned in the scope as I want the website to be great.

I have uploaded 2 Logo's and a 3D Logo will come through shortly.

Target Market(s)

People affected by a traumatic event in their lives needing assistance by professionals who are understanding and professionally trained

Coding

Coded - Design and coding required

Requirements
Must have
• *** Please note that correct wording for pages will only be supplied upon a successful winner for the finalization of the project.

I have domain names already but will need to be registered by the winner(i can supply the details I have received from NetHarbor).
Nice to have
• the feeling that we care because we do and that we are passionate for what we do.

```html
<!DOCTYPE html>
<html lang="en">
<head>
<meta charset="utf-8">
<title>Haven Restore – Trauma &amp; Cleanup Services</title>
<link rel="stylesheet" href="https://fonts.googleapis.com/css2?family=Michroma&family=Lato:wght@400;700&display=swap">
<style>
:root{
  --orange:#f15a24;
  --orange-light:#f7931e;
  --ink:#111;
  --text:#666;
  --grey-bg:#f2f2f2;
  --white:#fff;
  --footer:#000;
  --footer-bar:#1e1e1e;
}
*{box-sizing:border-box;margin:0;padding:0}
html,body{width:1200px;height:4098px;overflow:hidden}
body{position:relative;font-family:'Lato',sans-serif;color:var(--ink);background:var(--white)}
.abs{position:absolute}
.heading{font-family:'Michroma',sans-serif;font-weight:400;letter-spacing:0;text-transform:uppercase}
.btn{position:absolute;display:flex;align-items:center;justify-content:center;border-radius:20px;background:linear-gradient(90deg,var(--orange),var(--orange-light));color:#fff;font-size:11px;text-transform:uppercase;letter-spacing:.3px}
.brand{display:flex;align-items:center;gap:10px;color:var(--orange);font-family:'Michroma',sans-serif;font-size:14px}
.brand .dot{width:28px;height:28px;border-radius:50%;background:var(--orange)}
/* header */
.header{top:0;left:0;width:1200px;height:107px}
.header .brand{position:absolute;left:150px;top:38px}
.contact-chip{position:absolute;top:36px;display:flex;gap:12px;align-items:center}
.contact-chip .ico{width:36px;height:36px;border-radius:50%;background:var(--orange);display:flex;align-items:center;justify-content:center}
.contact-chip small{display:block;font-size:10px;color:#333}
.contact-chip b{font-size:13px;color:#222}
.nav{top:107px;left:0;width:1200px;height:53px;background:var(--ink)}
.nav a{position:absolute;top:0;height:53px;line-height:53px;color:#fff;font-size:14px;letter-spacing:3px;text-decoration:none}
.nav a.active{background:var(--orange);padding:0 20px}
/* hero */
.hero{top:160px;left:0;width:1200px;height:685px}
.hero-text{left:118px;top:262px;color:#fff}
.hero-text h1{font-size:25px;line-height:37px}
.hero-text p{font-size:13px;margin-top:22px}
/* about */
.about-photo{left:159px;top:926px;width:430px;height:430px;border-radius:50%;border:3px solid var(--orange);background:radial-gradient(circle at 55% 50%,#c69a5a,#6b4522 70%,#3a2614)}
.divider-left{display:flex;align-items:center;gap:6px}
.divider-left span{width:140px;height:1px;background:#333}
.body-copy{font-size:13px;line-height:22.5px;color:var(--text)}
/* services */
.services{top:1435px;left:0;width:1200px;height:798px;background:var(--grey-bg)}
.section-title{width:1200px;text-align:center;font-size:22px}
.divider{position:absolute;left:0;width:1200px;display:flex;justify-content:center;align-items:center;gap:14px}
.divider span{width:100px;height:1px;background:#555}
.service{position:absolute;top:208px;width:314px;text-align:center}
.service .circle{width:74px;height:74px;border-radius:50%;background:#e6e6e6;margin:48px auto 0;display:flex;align-items:center;justify-content:center}
.service h3{font-size:11px;line-height:16px;margin-top:24px;height:34px}
.service p{font-size:13px;line-height:22.5px;color:var(--text);margin:24px auto 0;width:236px}
.service a{display:inline-block;margin-top:20px;font-size:13px;color:var(--orange);text-decoration:underline}
.service.featured{background:var(--white);height:369px;border-bottom:4px solid var(--ink);box-shadow:0 4px 16px rgba(0,0,0,.12);border-radius:6px 6px 0 0}
.next{left:1099px;top:1820px;width:44px;height:44px;border-radius:50%;background:#fff;box-shadow:0 2px 8px rgba(0,0,0,.15);display:flex;align-items:center;justify-content:center}
/* band */
.band{top:2233px;left:0;width:1200px;height:462px}
.band-text{left:145px;top:98px;color:#fff}
.band-text h2{font-size:22px;line-height:32px}
.band-text p{font-size:13px;line-height:22.5px;margin-top:28px;width:450px}
/* reviews */
.reviews{top:2695px;left:0;width:1200px;height:471px;background:var(--grey-bg)}
.quote{left:197px;top:208px;width:835px;text-align:center;font-size:12.5px;line-height:22.5px;color:var(--text)}
.qmark{font-family:Georgia,serif;font-size:52px;color:#777}
.dots{left:0;width:1200px;top:388px;display:flex;justify-content:center;gap:14px}
.dots i{width:9px;height:9px;border-radius:50%;background:#111}
.dots i:first-child{background:var(--orange)}
/* contact */
.field{position:absolute;background:#f0f0f0;border-radius:18px;font-size:11px;color:#444;padding:12px 22px}
/* footer */
.footer{top:3590px;left:0;width:1200px;height:508px}
.footer-col{position:absolute;top:210px;color:#fff}
.footer-col h4{font-size:12px;font-weight:400}
.footer-col .lines{font-size:13px;line-height:16px;margin-top:60px}
.copy-bar{position:absolute;left:0;top:450px;width:1200px;height:58px;background:var(--footer-bar);color:#fff;font-size:13px}
.social{position:absolute;top:20px;display:flex;gap:14px;left:888px}
.social i{width:21px;height:21px;border-radius:50%;background:var(--orange)}
</style>
</head>
<body>

<header class="abs header">
  <div class="brand"><span class="dot"></span>HAVEN RESTORE</div>
  <div class="contact-chip" style="left:608px">
    <div class="ico"><svg width="16" height="16" viewBox="0 0 24 24"><path fill="#fff" d="M6.6 10.8a15 15 0 0 0 6.6 6.6l2.2-2.2a1 1 0 0 1 1-.25 11.4 11.4 0 0 0 3.6.6 1 1 0 0 1 1 1V20a1 1 0 0 1-1 1A17 17 0 0 1 3 4a1 1 0 0 1 1-1h3.5a1 1 0 0 1 1 1c0 1.25.2 2.45.6 3.6a1 1 0 0 1-.25 1z"/></svg></div>
    <div><small>CALL US NOW</small><b>+00 123 456 789</b></div>
  </div>
  <div class="contact-chip" style="left:797px">
    <div class="ico"><svg width="16" height="16" viewBox="0 0 24 24"><path fill="#fff" d="M3 5h18v14H3z"/><path d="M3 5l9 7 9-7" fill="none" stroke="#f15a24" stroke-width="2"/></svg></div>
    <div><small>MAIL US</small><b>info@havenrestore.com</b></div>
  </div>
</header>

<nav class="abs nav">
  <a class="active" style="left:262px;width:91px">HOME</a>
  <a style="left:378px">ABOUT US</a>
  <a style="left:510px">SERVICES</a>
  <a style="left:635px">TESTIMONIALS</a>
  <a style="left:805px">CONTACT US</a>
</nav>

<section class="abs hero">
  <svg width="1200" height="685" viewBox="0 0 1200 685" class="abs" style="left:0;top:0">
    <defs>
      <linearGradient id="heroTone" x1="0" y1="0" x2="1" y2="0">
        <stop offset="0" stop-color="#5c5a55"/><stop offset=".55" stop-color="#8d8b86"/><stop offset="1" stop-color="#b9b7b2"/>
      </linearGradient>
      <linearGradient id="swoosh" x1="0" y1="0" x2="1" y2="0">
        <stop offset="0" stop-color="#f7931e"/><stop offset="1" stop-color="#f15a24"/>
      </linearGradient>
    </defs>
    <rect width="1200" height="685" fill="url(#heroTone)" role="img" aria-label="Photo of a cleaner in a white protective suit holding a respirator mask"/>
    <path d="M0 585 Q 560 790 1200 545 L1200 685 L0 685Z" fill="url(#swoosh)"/>
    <path d="M0 640 Q 600 790 1200 565 L1200 685 L0 685Z" fill="#fff"/>
  </svg>
  <div class="abs hero-text">
    <h1 class="heading">Trusted<br>Trauma &amp; Cleanup Services</h1>
    <p>24/7 Crime Scene Cleanning service</p>
  </div>
  <span class="btn" style="left:118px;top:384px;width:123px;height:32px">Read More</span>
</section>

<section>
  <div class="abs about-photo" role="img" aria-label="Photo of two technicians scrubbing a damaged wooden floor"></div>
  <h2 class="abs heading" style="left:640px;top:958px;font-size:22px">About Us</h2>
  <div class="abs divider-left" style="left:640px;top:1002px">
    <svg width="16" height="20" viewBox="0 0 16 20"><path d="M8 0c1 5 7 7 7 13a7 7 0 0 1-14 0c0-3 2-5 3-6 0 2 1 3 2 3 0-4 1-7 2-10z" fill="#f15a24"/></svg><span></span>
  </div>
  <p class="abs body-copy" style="left:644px;top:1046px;width:405px">Lorem Ipsum is simply dummy text of the printing and typesetting industry. Lorem Ipsum has been the industry's standard dummy text ever since the 1500s, when an unknown printer took a galley of type and scrambled it to make a type specimen book. It has survived not only five centuries, but also the leap into electronic typesetting, remaining essentially unchanged.</p>
  <p class="abs body-copy" style="left:644px;top:1203px;width:405px">It was popularised in the 1960s with the release of Varnell sheets containing Lorem Ipsum passages, and more recently with desktop publishing software like Pagecraft Studio including versions of Lorem Ipsum.</p>
  <span class="btn" style="left:644px;top:1322px;width:123px;height:33px">Read More</span>
</section>

<section class="abs services">
  <h2 class="abs heading section-title" style="top:86px">Our Services</h2>
  <div class="divider" style="top:145px"><span></span><svg width="16" height="20" viewBox="0 0 16 20"><path d="M8 0c1 5 7 7 7 13a7 7 0 0 1-14 0c0-3 2-5 3-6 0 2 1 3 2 3 0-4 1-7 2-10z" fill="#f15a24"/></svg><span></span></div>
  <div class="service" style="left:115px">
    <div class="circle"><svg width="24" height="30" viewBox="0 0 16 20"><path d="M8 0c1 5 7 7 7 13a7 7 0 0 1-14 0c0-3 2-5 3-6 0 2 1 3 2 3 0-4 1-7 2-10z" fill="#f15a24"/></svg></div>
    <h3 class="heading">Fire &amp; Smoke Restoration</h3>
    <p>Lorem Ipsum is simply dummy text of the printing and typesetting industry. Lorem Ipsum has been the industry's standard dummy text.</p>
    <a>READ MORE</a>
  </div>
  <div class="service featured" style="left:441px">
    <div class="circle"><svg width="30" height="30" viewBox="0 0 30 30"><circle cx="15" cy="15" r="12" fill="#f15a24"/><path d="M15 8c2 4 5 6 5 9a5 5 0 0 1-10 0c0-3 3-5 5-9z" fill="#fff"/></svg></div>
    <h3 class="heading">Water Restoration/<br>Mould Remediation</h3>
    <p>Lorem Ipsum is simply dummy text of the printing and typesetting industry. Lorem Ipsum has been the industry's standard dummy text.</p>
    <a>READ MORE</a>
  </div>
  <div class="service" style="left:771px">
    <div class="circle"><svg width="30" height="30" viewBox="0 0 30 30"><path d="M24 4 15 17" stroke="#f15a24" stroke-width="3"/><path d="M12 14l6 5-5 7-8-6z" fill="#f15a24"/></svg></div>
    <h3 class="heading">Hoarding &amp; Squalor<br>Cleaning</h3>
    <p>Lorem Ipsum is simply dummy text of the printing and typesetting industry. Lorem Ipsum has been the industry's standard dummy text.</p>
    <a>READ MORE</a>
  </div>
  <span class="btn" style="left:528px;top:653px;width:143px;height:33px">View All Services</span>
</section>
<div class="abs next"><svg width="12" height="16" viewBox="0 0 12 16"><path d="M3 2l6 6-6 6" fill="none" stroke="#f15a24" stroke-width="2"/></svg></div>

<section class="abs band">
  <svg width="1200" height="462" class="abs" style="left:0;top:0">
    <defs><linearGradient id="bandTone" x1="0" y1="0" x2="1" y2="0"><stop offset="0" stop-color="#2f3438"/><stop offset=".5" stop-color="#3f454a"/><stop offset="1" stop-color="#6d7378"/></linearGradient></defs>
    <rect width="1200" height="462" fill="url(#bandTone)" role="img" aria-label="Photo of a technician in protective suit and mask working at a taped-off scene"/>
    <path d="M565 462 L830 0 L1200 0 L1200 462Z" fill="#8a9095" opacity=".45"/>
  </svg>
  <div class="abs band-text">
    <h2 class="heading">Crime Scene Cleaning Company<br>That Cares</h2>
    <p>Lorem Ipsum is simply dummy text of the printing and typesetting industry. Lorem Ipsum has been the industry's standard dummy text ever since the 1500s, when an unknown printer took a galley of type and scrambled it to make a type specimen book. It has survived not only five centuries, but also the leap into electronic typesetting, remaining essentially unchanged.</p>
  </div>
  <span class="btn" style="left:150px;top:335px;width:142px;height:32px">Contact Us Now</span>
</section>

<section class="abs reviews">
  <h2 class="abs heading section-title" style="top:104px">Clients`s Reviews</h2>
  <div class="divider" style="top:157px"><span></span><svg width="16" height="20" viewBox="0 0 16 20"><path d="M8 0c1 5 7 7 7 13a7 7 0 0 1-14 0c0-3 2-5 3-6 0 2 1 3 2 3 0-4 1-7 2-10z" fill="#f15a24"/></svg><span></span></div>
  <span class="abs qmark" style="left:165px;top:190px">&ldquo;</span>
  <p class="abs quote">Lorem Ipsum is simply dummy text of the printing and typesetting industry. Lorem Ipsum has been the industry's standard dummy text ever since the 1500s, when an unknown printer took a galley of type and scrambled it to make a type specimen book. It has survived not only five centuries, but also the leap into electronic typesetting, remaining essentially unchanged.</p>
  <span class="abs qmark" style="left:878px;top:245px">&rdquo;</span>
  <div class="abs" style="left:0;width:1200px;top:308px;text-align:center;color:#f5c400;font-size:11px;letter-spacing:1px">★★★★★</div>
  <div class="abs heading" style="left:0;width:1200px;top:348px;text-align:center;font-size:15px">Martin Ellery</div>
  <div class="abs dots"><i></i><i></i><i></i><i></i></div>
</section>

<section>
  <h2 class="abs heading section-title" style="top:3228px">Contact Us</h2>
  <div class="divider" style="top:3278px"><span></span><svg width="16" height="20" viewBox="0 0 16 20"><path d="M8 0c1 5 7 7 7 13a7 7 0 0 1-14 0c0-3 2-5 3-6 0 2 1 3 2 3 0-4 1-7 2-10z" fill="#f15a24"/></svg><span></span></div>
  <div class="field" style="left:309px;top:3320px;width:280px;height:32px">Full Name*</div>
  <div class="field" style="left:604px;top:3320px;width:281px;height:32px">Phone*</div>
  <div class="field" style="left:309px;top:3365px;width:576px;height:32px">Email Address*</div>
  <div class="field" style="left:309px;top:3410px;width:576px;height:102px">Your Message*</div>
  <span class="btn" style="left:543px;top:3535px;width:111px;height:33px">Send Now</span>
</section>

<footer class="abs footer">
  <svg width="1200" height="508" class="abs" style="left:0;top:0">
    <defs><linearGradient id="footSwoosh" x1="0" y1="0" x2="1" y2="0"><stop offset="0" stop-color="#f7931e"/><stop offset="1" stop-color="#e8401c"/></linearGradient></defs>
    <path d="M0 205 Q 420 40 1200 12 L1200 50 Q 480 70 0 210Z" fill="url(#footSwoosh)"/>
    <path d="M0 215 Q 480 70 1200 55 L1200 508 L0 508Z" fill="#000"/>
  </svg>
  <div class="footer-col" style="left:150px;top:205px">
    <div class="brand" style="font-size:12px"><span class="dot" style="width:22px;height:22px"></span>HAVEN RESTORE</div>
    <p class="lines" style="margin-top:52px;width:215px">Lorem Ipsum is simply dummy text of the printing and typesetting industry.</p>
  </div>
  <div class="footer-col" style="left:411px">
    <h4 class="heading">Quick Links</h4>
    <p class="lines">Home<br>About us<br>Services<br>Testimonials<br>Contact us</p>
  </div>
  <div class="footer-col" style="left:572px">
    <h4 class="heading">Contact&nbsp; Info</h4>
    <p class="lines"><span style="color:var(--orange)">●</span> +00 123 456 789<br><span style="color:var(--orange)">●</span> info@havenrestore.com<br><br><span style="color:var(--orange)">●</span> 214 Alder Crest Rd.<br>&nbsp;&nbsp;&nbsp;&nbsp;Fairmont, IL 60412</p>
  </div>
  <div class="footer-col" style="left:819px">
    <h4 class="heading">Newsletter</h4>
  </div>
  <div class="field" style="left:817px;top:280px;width:232px;height:33px;background:#fff;font-size:10px">Email Address*</div>
  <span class="btn" style="left:817px;top:333px;width:111px;height:32px">Subscribe</span>
  <div class="copy-bar">
    <p style="position:absolute;left:150px;top:21px">Copyright © 2020 Haven Restore Services.All Rights Reserved.</p>
    <div class="social"><i></i><i></i><i></i><i></i><i></i></div>
  </div>
</footer>

</body>
</html>
```